Website for Company to help with House Restoration from Hurricane Damage

Crisp, Clean and Professional!

I need a FRONT page for a website. I need it created in photoshop with the layers intact. We DO NOT need the HTML or RBT for the site. Simply the design. Any fonts you use will need to be included if they are not standard. Please make sure any fonts you use in the body of the text are available for use on Google Fonts.

I have attached a word doc that lists the menu items and additional instructions.

A little about the company - after Hurricane Quintessa - RBT developed a system which allows the house to be raised, the Pylonets installed, and the house reset on the Pylonets without the expense of moving the house or driving new pilings. This option can be installed in a matter of days with limited space and at a lower construction cost.

Please refer to the attached musthaves.doc and images that are included.

The main page must incorporate the menu, the attached photos w/ text underneath (text is in the word doc attached), and the text included in the word doc.

Standard footer with contact info as well.

If you have questions please contact us!
Updates

Designs are due by Friday! We will pick one this weekend.  We are unable to change it from 10 days to 5.  Thank you!!!

Target Market(s)

People who lost their homes or businesses due to a hurricane.

Industry/Entity Type

Construction

Requirements
Must have
• See attached musthaves.doc

```html
<!DOCTYPE html>
<html lang="en">
<head>
<meta charset="utf-8">
<title>Resilient Base Technologies — Rebuild Safer, Stronger, Better</title>
<link rel="stylesheet" href="https://fonts.googleapis.com/css2?family=Roboto:wght@400;500;700&family=Signika:ital,wght@0,400;0,500;1,400&display=swap">
<style>
  :root {
    --sky-top: #7d7390;
    --sky-glow: #d9a08e;
    --water: #6c7a93;
    --sand: #4f5566;
    --nav-bg: rgba(24, 30, 40, 0.82);
    --nav-shelf: #7b7d82;
    --accent: #8fa45b;
    --accent-dark: #6e8440;
    --logo-bg: #c6d7a1;
    --logo-bg-top: #e3ecd0;
    --text: #55595f;
    --white: #ffffff;
    --footer-top: #8e9e5e;
    --footer-bottom: #c9d9a3;
    --footer-text: #1d1f22;
  }
  * { box-sizing: border-box; margin: 0; padding: 0; }
  html, body { width: 1200px; height: 1046px; overflow: hidden; background: var(--white); }
  body { position: relative; font-family: "Roboto", Arial, sans-serif; }

  .hero {
    position: absolute; left: 0; top: 0; width: 1200px; height: 553px;
    background:
      radial-gradient(ellipse 220px 90px at 605px 75px, rgba(255, 214, 160, 0.9), transparent 70%),
      linear-gradient(180deg, var(--sky-top) 0%, var(--sky-glow) 13%, #9c8ea0 16%, var(--water) 30%, #5d6a84 52%, var(--sand) 68%, #3f4352 100%);
  }
  .hero__headline {
    position: absolute; left: 48px; top: 284px;
    font-family: "Signika", "Trebuchet MS", sans-serif;
    font-size: 48px; line-height: 43px; color: var(--white); font-weight: 400;
    text-shadow: 0 1px 3px rgba(0,0,0,0.3);
  }
  .hero__headline em { font-style: italic; }

  .brand {
    position: absolute; left: 972px; top: 0; width: 180px; height: 198px;
    background: linear-gradient(180deg, var(--logo-bg-top), var(--logo-bg));
    border-radius: 0 0 10px 10px;
    display: flex; align-items: center; justify-content: center;
    font-family: "Signika", "Trebuchet MS", sans-serif;
    font-weight: 500; font-size: 58px; color: #2e3a22;
  }

  .nav-shadow {
    position: absolute; left: 70px; top: 560px; width: 1060px; height: 22px;
    background: rgba(0,0,0,0.18); filter: blur(10px); border-radius: 50%;
  }
  .main-nav {
    position: absolute; left: 48px; top: 445px; width: 1104px; height: 108px;
    background: var(--nav-bg);
  }
  .main-nav__shelf {
    position: absolute; left: 48px; top: 553px; width: 1104px; height: 12px;
    background: var(--nav-shelf);
  }
  .main-nav ul {
    list-style: none; display: flex; justify-content: center; align-items: center;
    height: 100%;
  }
  .main-nav li {
    position: relative; color: var(--white); font-weight: 500; font-size: 19px;
    display: flex; align-items: center;
  }
  .main-nav li + li::before {
    content: ""; width: 4px; height: 4px; border-radius: 50%;
    background: var(--accent); margin: 0 27px;
  }
  .main-nav .is-active .marker {
    position: absolute; left: 50%; width: 58px; height: 14px; transform: translateX(-50%);
  }
  .main-nav .is-active .marker--top { top: -54px; }
  .main-nav .is-active .marker--bottom { bottom: -54px; }

  .intro {
    position: absolute; left: 72px; top: 608px; width: 1056px;
    display: grid; grid-template-columns: 498px 498px; column-gap: 60px;
  }
  .intro p {
    font-size: 17.4px; line-height: 24px; color: var(--text); text-align: justify;
  }
  .intro a { color: var(--accent-dark); font-weight: 700; text-decoration: underline; }

  .site-footer {
    position: absolute; left: 0; top: 928px; width: 1200px; height: 118px;
    background: linear-gradient(180deg, var(--footer-top) 0%, var(--footer-bottom) 55%, var(--footer-bottom) 100%);
    padding: 27px 0 0 49px;
    font-size: 13.6px; line-height: 16.6px; color: var(--footer-text);
  }
  .site-footer strong { font-weight: 700; }
</style>
</head>
<body>
  <div class="hero" role="img" aria-label="Photograph of a parent crouching with a small child on a beach at sunset, boats on the calm water behind"></div>
  <h1 class="hero__headline">Rebuild Safer,<br>Stronger, Better<br><em>to build new lasting memories.</em></h1>

  <div class="brand">RBT</div>

  <div class="nav-shadow"></div>
  <nav class="main-nav">
    <ul>
      <li>Home</li>
      <li class="is-active"><span>Services
        <svg class="marker marker--top" viewBox="0 0 58 14"><polygon points="0,0 58,0 29,14" fill="#8fa45b"/></svg>
        <svg class="marker marker--bottom" viewBox="0 0 58 14"><polygon points="29,0 58,14 0,14" fill="#8fa45b"/></svg>
      </span></li>
      <li>About Us</li>
      <li>Product Specifications</li>
      <li>Design Documentation</li>
      <li>Contact Us</li>
    </ul>
  </nav>
  <div class="main-nav__shelf"></div>

  <section class="intro">
    <p>Systems for extending the height of existing piles are not available on today’s market. Resilient Base Technologies, LLC (RBT) has developed two systems to allow for Piles to be extended that provide superior structural support without corrosion and maintenance concerns. We provided two systems, a complete system, Pile Cap Extension Pylonets, and Pile Splice. These two systems allow a home to be raised to by up to 54”, higher extensions possible with additional design consideration for lateral support. Shown below is the full Piling Extension system, which connects to the top of the existing pile. The system modular and can be cut to meet specific needs of the home.</p>
    <p>Our Patented Piling system has been designed to withstand the corrosive environment of beach communities. The salt water and windblown sand corrodes unprotected materials, and yes, even stainless steel. Our system utilizes a high strength carbon fiber material that is corrosion proof from salt water and UV proof. The system will not erode, decay or loose strength over time. The system has three installation conditions, for raising a house on existing pilings, repairing damaged pilings, and for connecting new pilings to floor joists in new construction. The three options are generally described <a href="#">here</a>.</p>
  </section>

  <footer class="site-footer">
    <strong>Resilient Base Technologies, LLC</strong><br>
    PO Box 41520,&nbsp; Harbor Point, NJ 08099-0040<br>
    (555) 014-2290<br>
    sales@resilientbase.example
  </footer>
</body>
</html>
```